Dorrington Thermal Heating and Air Conditioning web page

This is a repair, installation and maintenance residential company. I don't do commercial. I need a web design that shows a company with 24/7 fast service that is easy for customers to contact me from. I am a Brackley /Tovex HVAC dealer and their logos can be on there also. I also sell IAQ products like Zenta- Orbit and I offer duct cleanings as well.

Industry/Entity Type

Hvac

Coding

Coded - Design and coding required

Number of Pages Required

2 page

```html
<!DOCTYPE html>
<html lang="en">
<head>
<meta charset="utf-8">
<title>Dorrington Thermal Heating and Air Conditioning</title>
<link href="https://fonts.googleapis.com/css2?family=Poppins:wght@300;400;500;600&display=swap" rel="stylesheet">
<style>
:root{
  --blue:#00a8e8;
  --blue-dark:#0d8fd0;
  --red:#e3141c;
  --ink:#1c1c1c;
  --text:#555;
  --muted:#888;
  --grey-band:#efefef;
  --white:#fff;
  --backdrop:#e9ecef;
}
*{box-sizing:border-box;margin:0;padding:0}
html,body{width:1200px;height:2659px;overflow:hidden}
body{background:var(--backdrop);font-family:'Poppins',sans-serif;color:var(--ink)}
.page{position:absolute;left:135px;top:160px;width:940px;height:2314px;background:var(--white);box-shadow:0 10px 40px rgba(0,0,0,.12);overflow:hidden}
.abs{position:absolute}
.section{position:absolute;left:0;width:940px}
.brand{font-weight:600;font-size:15px;line-height:1.05;color:var(--ink);letter-spacing:.2px}
.brand small{display:block;font-size:15px}
/* header */
.header{top:0;height:66px}
.contact{display:flex;gap:6px;font-size:8.5px;color:var(--muted);line-height:1.25}
.contact svg{flex:none;margin-top:1px}
.social-ring{width:28px;height:28px;border:1.5px solid #999;border-radius:50%}
/* nav */
.nav{top:66px;height:47px;background:var(--blue);display:flex;justify-content:center;align-items:center;gap:25px;font-size:10px;font-weight:500;color:var(--white)}
.nav .current{font-weight:600}
/* hero */
.hero{top:113px;height:342px;background:#efefef}
.hero-photo{right:0;top:0;width:538px;height:342px;background:linear-gradient(110deg,#f2f2f2 0%,#e6e7e9 45%,#d9d4cf 80%,#ece9e6 100%)}
.hero h1{left:116px;top:82px;font-size:37px;font-weight:500;line-height:39px;color:var(--ink)}
.red{color:var(--red)}
.blue{color:var(--blue)}
.btn{display:inline-flex;align-items:center;justify-content:center;background:var(--blue);color:var(--white);border-radius:16px;font-weight:500}
.hero .btn{left:116px;top:220px;width:133px;height:31px;font-size:13px}
.dots{display:flex;gap:4px}
.dot{width:8px;height:8px;border-radius:50%;border:1px solid #999}
.dot.on{border-color:var(--red)}
/* features */
.features{top:455px;height:196px}
.feature{position:absolute;top:51px;width:110px;text-align:center;font-size:8.5px;font-weight:500;line-height:1.1}
.feature .ring{width:68px;height:68px;margin:0 auto 8px;border-radius:50%;background:#efefef;display:flex;align-items:center;justify-content:center}
/* quality */
.quality{top:651px;height:331px;background:var(--grey-band)}
.quality h2{left:116px;top:76px;font-size:20px;font-weight:500;line-height:19px}
.body-copy{font-size:7.5px;color:var(--muted);line-height:1.6}
.quality .btn{left:116px;top:224px;width:76px;height:24px;font-size:8.5px}
.photo{border-radius:12px}
/* help */
.help{top:982px;height:394px}
.center{left:0;width:940px;text-align:center}
.help h2{top:50px;font-size:19px;font-weight:500}
.help .sub{top:82px;font-size:11px;color:var(--muted)}
.tab{top:107px;height:29px;border-radius:15px;display:flex;align-items:center;justify-content:center;gap:6px;font-size:9.5px}
.tab.on{background:var(--blue);color:var(--white)}
.tab.off{background:#eee;color:var(--muted)}
.card{position:absolute;top:160px;width:168px;text-align:center}
.card .img{height:117px}
.card h3{margin-top:23px;font-size:10.5px;font-weight:500}
.card p{margin-top:4px;font-size:7.5px;color:var(--muted);line-height:1.3;padding:0 10px}
.card a{display:block;margin-top:4px;font-size:8px;color:var(--blue);text-decoration:none}
/* band */
.band{top:1376px;height:99px;background:var(--blue)}
.band .line{left:190px;top:37px;font-size:19px;font-weight:500;color:var(--white)}
.band .quote{left:584px;top:35px;width:164px;height:34px;border-radius:17px;background:var(--white);color:var(--blue);font-size:13px;display:flex;align-items:center;justify-content:center}
/* stats */
.stats{top:1475px;height:165px;background:var(--grey-band)}
.stat{position:absolute;top:38px;width:200px;text-align:center}
.stat b{display:block;font-size:49px;font-weight:500;color:var(--blue);line-height:1}
.stat span{display:block;margin-top:14px;font-size:10px;color:var(--text)}
/* blog */
.blog{top:1640px;height:386px}
.blog h2{top:44px;font-size:19px;font-weight:500}
.post{position:absolute;top:101px;width:350px;height:163px;background:#efefef}
.post .img{left:16px;top:17px;width:130px;height:130px}
.post .txt{left:160px;top:40px;width:175px}
.post h4{font-size:9.5px;font-weight:500;color:#1a3b78;line-height:1.1}
.post .meta{margin-top:9px;font-size:6.5px;color:var(--muted)}
.post p{margin-top:9px;font-size:6.5px;color:var(--muted);line-height:1.5}
.post a{display:inline-block;margin-top:9px;font-size:8px;color:var(--red);text-decoration:none;border-bottom:1px solid var(--red);padding-bottom:1px}
/* testimonial + footer */
.lower{top:2026px;height:288px;background:var(--grey-band)}
.avatar{left:436px;top:-34px;width:68px;height:68px;border-radius:50%;background:radial-gradient(circle at 50% 40%,#d9c5b5,#5c6670);border:3px solid var(--white)}
.quote-text{left:290px;top:78px;width:360px;text-align:center;font-size:6.7px;color:var(--muted);line-height:1.6}
.footer-links{left:116px;top:228px;display:flex;gap:21px;font-size:10px;color:var(--text)}
.footer-links .current{color:var(--blue)}
.copy{left:116px;top:250px;font-size:7px;color:var(--muted)}
.copy em{font-style:normal;color:var(--blue)}
.subscribe{left:600px;top:188px;width:226px;height:23px;border-radius:12px;background:var(--white);border:1px solid #ddd}
.subscribe span{position:absolute;left:14px;top:6px;font-size:8px;color:var(--muted)}
.subscribe b{position:absolute;right:-1px;top:-1px;width:74px;height:23px;border-radius:12px;background:var(--blue);color:var(--white);font-size:8px;font-weight:500;display:flex;align-items:center;justify-content:center}
.social-dot{width:20px;height:20px;border-radius:50%;background:var(--blue)}
</style>
</head>
<body>
<div class="page">

  <header class="section header">
    <div class="abs brand" style="left:116px;top:15px">Dorrington<small>Thermal</small></div>
    <div class="abs contact" style="left:304px;top:23px">
      <svg width="9" height="11" viewBox="0 0 9 11"><path d="M4.5 10.5S1 6.6 1 4.3a3.5 3.5 0 0 1 7 0c0 2.3-3.5 6.2-3.5 6.2z" fill="var(--red)"/><circle cx="4.5" cy="4.2" r="1.3" fill="#fff"/></svg>
      <div>2210 Harbor Lane,<br>Elmwood, NJ</div>
    </div>
    <div class="abs contact" style="left:448px;top:23px">
      <svg width="10" height="10" viewBox="0 0 10 10"><circle cx="5" cy="5" r="4.5" fill="var(--red)"/><path d="M5 2.5V5h2" stroke="#fff" stroke-width="1" fill="none"/></svg>
      <div>Monday-Friday<br>8:00 am - 8:00 pm</div>
    </div>
    <div class="abs contact" style="left:588px;top:23px">
      <svg width="10" height="10" viewBox="0 0 10 10"><path d="M2 .8l2 2-1 1.2a6 6 0 0 0 3 3l1.2-1 2 2-1.4 1.4C4.5 9 1 5.5.6 2.2z" fill="var(--red)"/></svg>
      <div>24/7 Emergency Service<br>555-014-2290</div>
    </div>
    <div class="abs social-ring" style="left:735px;top:19px"></div>
    <div class="abs social-ring" style="left:768px;top:19px"></div>
    <div class="abs social-ring" style="left:801px;top:19px"></div>
  </header>

  <nav class="section nav">
    <span class="current">HOME</span><span>About Us</span><span>Services</span><span>Blogs</span><span>FAQs</span><span>Contact us</span>
    <svg class="abs" style="left:796px;top:16px" width="15" height="15" viewBox="0 0 15 15"><circle cx="6" cy="6" r="4.8" stroke="#fff" stroke-width="1.6" fill="none"/><path d="M9.5 9.5l4 4" stroke="#fff" stroke-width="1.6"/></svg>
    <svg class="abs" style="left:826px;top:16px" width="4" height="15" viewBox="0 0 4 15"><circle cx="2" cy="2" r="1.6" fill="#fff"/><circle cx="2" cy="7.5" r="1.6" fill="#fff"/><circle cx="2" cy="13" r="1.6" fill="#fff"/></svg>
  </nav>

  <section class="section hero">
    <div class="abs hero-photo" role="img" aria-label="Technician fitting the front cover on a wall-mounted split air conditioner"></div>
    <h1 class="abs"><span class="red">Heating</span> and <span class="blue">Air</span><br><span class="blue">Conditioning</span><br>Specialist</h1>
    <span class="abs btn">Appointment</span>
    <div class="abs dots" style="left:452px;top:308px"><i class="dot on"></i><i class="dot"></i><i class="dot"></i></div>
  </section>

  <section class="section features">
    <div class="feature" style="left:161px"><div class="ring"><svg width="30" height="30" viewBox="0 0 30 30" fill="none" stroke="var(--blue)" stroke-width="1.3"><ellipse cx="11" cy="8" rx="8" ry="3"/><path d="M3 8v12c0 1.7 3.6 3 8 3"/><path d="M3 12c0 1.7 3.6 3 8 3M3 16c0 1.7 3.6 3 8 3"/><circle cx="20" cy="19" r="7"/><path d="M22 16.5h-3a1.3 1.3 0 0 0 0 2.6h2a1.3 1.3 0 0 1 0 2.6h-3M20 15v1.5M20 21.7v1.5"/></svg></div>No Upfront<br>Payments</div>
    <div class="feature" style="left:286px"><div class="ring"><svg width="30" height="30" viewBox="0 0 30 30" fill="none" stroke="var(--blue)" stroke-width="1.3"><rect x="4" y="14" width="5" height="11"/><path d="M9 15l4-6V5h2a2 2 0 0 1 2 2v5h6a2 2 0 0 1 2 2l-2 9a2 2 0 0 1-2 2H9"/><path d="M20 3l1-2M23 6l2-1M17 2V0"/></svg></div>Satisfcation<br>Guarantee</div>
    <div class="feature" style="left:411px"><div class="ring"><svg width="30" height="30" viewBox="0 0 30 30" fill="none" stroke="var(--blue)" stroke-width="1.3"><path d="M5 16v-3a10 10 0 0 1 20 0v3"/><rect x="3" y="15" width="4" height="7" rx="1"/><rect x="23" y="15" width="4" height="7" rx="1"/><circle cx="15" cy="16" r="6"/><text x="15" y="18.3" font-size="6" text-anchor="middle" fill="var(--blue)" stroke="none" font-family="Poppins,sans-serif">24</text><path d="M25 22c0 3-3 4-7 4"/></svg></div>Emergency<br>Services</div>
    <div class="feature" style="left:535px"><div class="ring"><svg width="30" height="30" viewBox="0 0 30 30" fill="none" stroke="var(--blue)" stroke-width="1.3"><path d="M2 12l6-5 5 2 4-2 6 4 5-3"/><path d="M8 7l-4 8 9 9 3-2 3 2 6-8"/><path d="M13 9l-4 5 2 1 4-3 5 5"/><path d="M12 19l2 2M15 17l2 2"/></svg></div>Fixed Right<br>Promise</div>
    <div class="feature" style="left:661px"><div class="ring"><svg width="30" height="30" viewBox="0 0 30 30" fill="none" stroke="var(--blue)" stroke-width="1.3"><circle cx="15" cy="11" r="8"/><circle cx="15" cy="11" r="5.5"/><path d="M15 8l1 2h2l-1.6 1.3.6 2.2-2-1.2-2 1.2.6-2.2L12 10h2z"/><path d="M10 17l-3 9 4-2 2 3 2-7M20 17l3 9-4-2-2 3-2-7"/></svg></div>8 Years<br>Experience</div>
  </section>

  <section class="section quality">
    <h2 class="abs">Quality <span class="red">Heating</span> &amp; <span class="blue">Cooling</span><br>Services</h2>
    <div class="abs body-copy" style="left:116px;top:128px;width:325px">Lorem Ipsum is simply dummy text of the printing and typesetting industry. Lorem Ipsum has been the industry's standard dummy text ever since the 1500s, when an unknown printer took a galley of type and scrambled it to make a type specimen book.</div>
    <div class="abs body-copy" style="left:116px;top:180px;width:325px">It has survived not only five centuries, but also the leap into electronic typesetting, remaining essentially unchanged.</div>
    <span class="abs btn">Read More</span>
    <div class="abs photo" role="img" aria-label="Plumber repairing pipes under a sink with a wrench" style="left:479px;top:63px;width:168px;height:205px;background:linear-gradient(160deg,#2f4d8c,#c8ccd3 55%,#e9e9ea)"></div>
    <div class="abs photo" role="img" aria-label="Technician testing an air conditioner unit with a multimeter" style="left:661px;top:63px;width:168px;height:205px;background:linear-gradient(170deg,#eceff1,#d3d8dc 60%,#b8b2a7)"></div>
  </section>

  <section class="section help">
    <h2 class="abs center">How Can We Help You?</h2>
    <div class="abs center sub">Choose Services</div>
    <div class="abs tab on" style="left:335px;width:132px"><svg width="11" height="11" viewBox="0 0 11 11" stroke="#fff" stroke-width="1"><path d="M5.5 0v11M0 5.5h11M1.6 1.6l7.8 7.8M9.4 1.6l-7.8 7.8"/></svg>Cooling Services</div>
    <div class="abs tab off" style="left:474px;width:132px"><svg width="12" height="12" viewBox="0 0 12 12" stroke="#999" stroke-width="1" fill="none"><circle cx="6" cy="6" r="2.5"/><path d="M6 0v2M6 10v2M0 6h2M10 6h2M1.8 1.8l1.4 1.4M8.8 8.8l1.4 1.4M10.2 1.8L8.8 3.2M3.2 8.8l-1.4 1.4"/></svg>Heating Services</div>
    <div class="card" style="left:116px"><div class="img" role="img" aria-label="Technician repairing an air conditioner with a screwdriver" style="background:linear-gradient(150deg,#dfe3e6,#9aa1a8 60%,#5c6269)"></div><h3>Air Conditioner Repair</h3><p>Lorem Ipsum is simply dummy text of the printing and typesetting.</p><a>Learn More</a></div>
    <div class="card" style="left:298px"><div class="img" role="img" aria-label="Technician installing an air conditioner with a meter" style="background:linear-gradient(150deg,#e6e8ea,#7c8ba0 55%,#3b4a66)"></div><h3>Installation</h3><p>Lorem Ipsum is simply dummy text of the printing and typesetting.</p><a>Learn More</a></div>
    <div class="card" style="left:480px"><div class="img" role="img" aria-label="Technician cleaning dust from an air conditioner" style="background:linear-gradient(150deg,#e9eaec,#5a5d63 55%,#2d2f33)"></div><h3>Dust Services</h3><p>Lorem Ipsum is simply dummy text of the printing and typesetting.</p><a>Learn More</a></div>
    <div class="card" style="left:661px"><div class="img" role="img" aria-label="Technician servicing a wall-mounted air conditioner" style="background:linear-gradient(150deg,#f3f4f5,#dfe2e4 55%,#c9ced2)"></div><h3>Maintenance</h3><p>Lorem Ipsum is simply dummy text of the printing and typesetting.</p><a>Learn More</a></div>
  </section>

  <section class="section band">
    <div class="abs line">No overtime charges, 7 days a week</div>
    <div class="abs quote">Get a Free Quote</div>
  </section>

  <section class="section stats">
    <div class="stat" style="left:126px"><b>5280</b><span>Unites Installed</span></div>
    <div class="stat" style="left:370px"><b>66%</b><span>Central Unites</span></div>
    <div class="stat" style="left:614px"><b>35%</b><span>Less Energy Used</span></div>
  </section>

  <section class="section blog">
    <h2 class="abs center">Latest Blog Post</h2>
    <article class="post" style="left:116px">
      <div class="abs img" role="img" aria-label="Group of students studying together outdoors" style="background:linear-gradient(140deg,#9bb56c,#d49a6a 50%,#4b6f9b)"></div>
      <div class="abs txt"><h4>The best online training during COVID-19 crisis</h4><div class="meta">by Dan Whitlow &nbsp;|&nbsp; Apr 07, 2020 at 3:13 pm &nbsp;|&nbsp; News</div><p>Lorem Ipsum is simply dummy text of the printing and typesetting industry. Lorem Ipsum has been</p><a>Read More</a></div>
    </article>
    <article class="post" style="left:479px">
      <div class="abs img" role="img" aria-label="Two people working together at a desk in an office" style="background:linear-gradient(140deg,#d9e4ea,#7f94a6 50%,#34404d)"></div>
      <div class="abs txt"><h4>The best online training during COVID-19 crisis</h4><div class="meta">by Dan Whitlow &nbsp;|&nbsp; Apr 07, 2020 at 3:13 pm &nbsp;|&nbsp; News</div><p>Lorem Ipsum is simply dummy text of the printing and typesetting industry. Lorem Ipsum has been</p><a>Read More</a></div>
    </article>
    <div class="abs" style="left:458px;top:394px;width:16px;height:4px;border-radius:2px;background:var(--red)"></div>
    <div class="abs" style="left:478px;top:394px;width:4px;height:4px;border-radius:50%;background:var(--blue)"></div>
  </section>

  <section class="section lower">
    <div class="abs avatar" role="img" aria-label="Portrait of a customer giving a testimonial"></div>
    <svg class="abs" style="left:236px;top:83px" width="14" height="24" viewBox="0 0 14 24"><path d="M12 2L2 12l10 10" stroke="var(--blue)" stroke-width="1.5" fill="none"/></svg>
    <svg class="abs" style="left:696px;top:88px" width="14" height="24" viewBox="0 0 14 24"><path d="M2 2l10 10L2 22" stroke="var(--blue)" stroke-width="1.5" fill="none"/></svg>
    <div class="abs quote-text">This practical home building resource will provide you with trusted information packaged in clear-cut instructions on the entire home building process from purchasing a building lot to scheduling every aspect of the build.</div>
    <div class="abs" style="left:456px;top:133px;display:flex;gap:5px"><i style="width:6px;height:6px;border-radius:50%;background:#bbb"></i><i style="width:6px;height:6px;border-radius:50%;background:var(--blue)"></i><i style="width:6px;height:6px;border-radius:50%;background:#bbb"></i></div>
    <div class="abs brand" style="left:116px;top:182px">Dorrington<small>Thermal</small></div>
    <div class="abs footer-links"><span class="current">Home</span><span>About Us</span><span>Services</span><span>Blogs</span><span>FAQs</span><span>Contact Us</span></div>
    <div class="abs copy">Copyright © 2020 Dorrington Thermal . <em>All Rights Reserved.</em></div>
    <div class="abs subscribe"><span>Type your email</span><b>Subscribe</b></div>
    <div class="abs social-dot" style="left:755px;top:228px"></div>
    <div class="abs social-dot" style="left:782px;top:228px"></div>
    <div class="abs social-dot" style="left:810px;top:228px"></div>
  </section>

</div>
</body>
</html>
```